Bright Sprout Sessions Brochure Project

Design a brochure that outlines the mindfulness programs I deliver and pricing. I will use this brochure to give to schools to promote my programs. Will have info about mindfulness and benefits, outline for each program I offer as well as prices and contact details. Contact details can be found at www.calmbrookhaven.com.au

Target Market(s)

Schools and community groups

Industry/Entity Type

Wellbeing and health

Font styles to use
Serif
Other font styles liked:
• open to suggestions

Colors
0094D4
00A9DD
6FCCEA
C7EBF8
E9F6FB

Requirements
Must have
• Title page, content as provided, my contact details and socials. Images and professional

```html
<!DOCTYPE html>
<html lang="en">
<head>
<meta charset="utf-8">
<title>Bright Sprout Sessions Brochure</title>
<link href="https://fonts.googleapis.com/css2?family=Amatic+SC:wght@700&family=Montserrat:wght@400;500;600&display=swap" rel="stylesheet">
<style>
  :root {
    --stage: #e6e9ea;
    --paper: #ffffff;
    --blue-deep: #0094d4;
    --blue: #00a9dd;
    --blue-mid: #6fccea;
    --blue-light: #c7ebf8;
    --blue-pale: #e9f6fb;
    --orange: #f39a1f;
    --orange-light: #fbc25a;
    --navy: #1f1d4a;
    --ink: #1d1d1f;
    --logo-ink: #6e93c8;
  }
  * { box-sizing: border-box; margin: 0; padding: 0; }
  html, body { width: 1200px; height: 900px; overflow: hidden; }
  body { background: var(--stage); font-family: "Montserrat", sans-serif; color: var(--ink); position: relative; }

  .page { position: absolute; background: var(--paper); box-shadow: 0 6px 22px rgba(0,0,0,.18); overflow: hidden; }
  .stripes { position: absolute; inset: 0; width: 100%; height: 100%; }

  /* Cover */
  .cover { left: 40px; top: 140px; width: 440px; height: 620px; }
  .brand-mark { position: absolute; left: 50%; transform: translateX(-50%); display: flex; flex-direction: column; align-items: center; gap: 10px; }
  .brand-mark .dot { border-radius: 50%; background: var(--blue-mid); border: 5px solid #d4d6d8; }
  .brand-mark .name { font-weight: 600; color: var(--orange); white-space: nowrap; }
  .cover .brand-mark { top: 100px; }
  .cover .brand-mark .dot { width: 150px; height: 150px; }
  .cover .brand-mark .name { font-size: 20px; }
  .cover-title { position: absolute; top: 330px; width: 100%; text-align: center; font-family: "Amatic SC", cursive; font-size: 62px; color: var(--orange); letter-spacing: 1px; }
  .cover-sub { position: absolute; top: 412px; width: 100%; text-align: center; font-size: 14px; font-weight: 500; line-height: 1.45; }
  .studio-mark { position: absolute; top: 470px; left: 50%; transform: translateX(-50%); display: flex; flex-direction: column; align-items: center; gap: 6px; }
  .studio-mark .ring { width: 70px; height: 70px; border-radius: 50%; border: 1.5px solid var(--logo-ink); }
  .studio-mark .name { font-size: 11px; font-weight: 500; color: var(--logo-ink); letter-spacing: 1.5px; text-transform: uppercase; }

  /* Spread */
  .spread-left { left: 510px; top: 220px; width: 330px; height: 480px; }
  .spread-right { left: 840px; top: 220px; width: 330px; height: 480px; }
  .mini-mark { position: absolute; top: 38px; right: 18px; display: flex; flex-direction: column; align-items: center; gap: 3px; }
  .mini-mark .dot { width: 34px; height: 34px; border-radius: 50%; background: var(--blue-mid); border: 2px solid #d4d6d8; }
  .mini-mark .name { font-size: 6px; font-weight: 600; color: var(--orange); white-space: nowrap; }
  .headline-band { position: absolute; top: 96px; left: 0; width: 100%; height: 110px; background: var(--navy); }
  .headline-band h2 { position: absolute; left: 16px; top: 38px; font-family: "Amatic SC", cursive; font-size: 30px; color: var(--orange); font-weight: 700; }
  .band-photo { position: absolute; right: 0; top: 0; width: 120px; height: 110px; background: linear-gradient(180deg, #6b6a86 0%, #b7aebf 55%, #c2367a 100%); }
  .body-copy { position: absolute; top: 218px; left: 16px; right: 16px; font-size: 6.6px; line-height: 1.45; text-align: justify; }
  .body-copy p + p { margin-top: 6px; }
  .folio { position: absolute; bottom: 16px; display: flex; align-items: center; gap: 8px; font-size: 8px; }
  .folio .ring { width: 24px; height: 24px; border-radius: 50%; border: 1px solid var(--logo-ink); }
  .spread-left .folio { left: 16px; }
  .spread-right .folio { left: 16px; color: #fff; }
  .spread-right .folio .ring { border-color: rgba(255,255,255,.7); }
  .full-photo { position: absolute; inset: 0; background: radial-gradient(circle at 45% 60%, #fff3d6 0%, #f7c58e 30%, #e39a6c 60%, #b36a52 100%); }
  .spread-right .mini-mark { top: 22px; }
</style>
</head>
<body>

<section class="page cover">
  <svg class="stripes" viewBox="0 0 440 620" preserveAspectRatio="none" aria-hidden="true">
    <polygon points="0,30 120,30 0,150" fill="var(--blue-deep)" opacity=".8"/>
    <polygon points="130,30 175,30 0,200 0,160" fill="var(--blue-mid)" opacity=".7"/>
    <polygon points="190,30 215,30 0,250 0,225" fill="var(--blue-light)"/>
    <polygon points="440,420 440,470 300,620 250,620" fill="var(--orange-light)" opacity=".6"/>
    <polygon points="440,500 440,620 330,620" fill="var(--orange)"/>
    <polygon points="440,470 440,490 320,620 300,620" fill="var(--orange-light)"/>
  </svg>
  <div class="brand-mark">
    <span class="dot"></span>
    <span class="name">Little Lantern Club</span>
  </div>
  <h1 class="cover-title">BRIGHT SPROUT SESSIONS</h1>
  <p class="cover-sub">Mindfulness and Positive Psychology<br>Programs for Children</p>
  <div class="studio-mark">
    <span class="ring"></span>
    <span class="name">Calm Brook Haven</span>
  </div>
</section>

<section class="page spread-left">
  <svg class="stripes" viewBox="0 0 330 480" preserveAspectRatio="none" aria-hidden="true">
    <polygon points="0,0 70,0 0,60" fill="var(--blue-deep)" opacity=".8"/>
    <polygon points="80,0 110,0 0,95 0,70" fill="var(--blue-mid)" opacity=".7"/>
    <polygon points="330,430 330,480 280,480" fill="var(--orange)"/>
    <polygon points="330,410 330,425 270,480 255,480" fill="var(--orange-light)"/>
  </svg>
  <div class="mini-mark"><span class="dot"></span><span class="name">Little Lantern Club</span></div>
  <div class="headline-band">
    <h2>MENTAL HEALTH MATTERS</h2>
    <div class="band-photo" role="img" aria-label="Photo of a child sitting alone in a pink armchair, seen from behind"></div>
  </div>
  <div class="body-copy">
    <p>Mindfulness has great potential as a key strategy for positively impacting on the mental and emotional wellbeing of children and young people. Research has shown that the potential benefits of mindfulness for children include reduction in stress, and anxiety symptoms, increases in calmness, self-esteem, self-acceptance, self-regulation and improved sleep quality.</p>
    <p>Mental illness is a major concern facing all Australians with almost one in seven 4-17 year-olds having a mental disorder in the previous 12 months. Furthermore, the recent pandemic added another complex array of factors such as uncertainty, social isolation, and parental angst. All of which have an impact on the mental health of children and adolescents.</p>
    <p>One in five adults will experience a 12-month mental disorder during their lifetime, with over two in five people facing some sort of mental health issue at some stage over their lifetime. Mental health is an essential part of children's overall health and wellbeing. It has a connected relationship with their physical health and their ability to succeed in school, at work and in society. As such the emotional wellbeing of children is just as important as their physical health. Good mental health allows children and young people to develop the resilience to cope with whatever life throws at them and grow into well-rounded, healthy and happy adults.</p>
    <p>With a focus on paying attention to the present moment, Mindfulness has beneficial effects on the emotional wellbeing, mental health, ability to learn and the physical health of children. Mindfulness training is one effective and cost-efficient way to promote healthy brain development and function, and foster stress resilience.</p>
  </div>
  <div class="folio"><span class="ring"></span><span>02</span></div>
</section>

<section class="page spread-right">
  <div class="full-photo" role="img" aria-label="Photo of an adult hand holding a child's hand against a glowing sunset sky with birds"></div>
  <div class="mini-mark"><span class="dot"></span><span class="name">Little Lantern Club</span></div>
  <div class="folio"><span class="ring"></span><span>03</span></div>
</section>

</body>
</html>
```